Billboard design for a small town Oral Surgeon

We are getting several billboards and need a design that highlights the doctors photo, and bullet points of what he does. Our business name is extremely long, so it’s a challenge to figure out how to do this. Maybe just use our logo? Open to ideas.
The logo can be shortened as designer sees fit, meaning we can drop the tag line. Important info to include:
Doctors name is Tobin Marek
The highlighted bullet points are:
•Implants
•wisdom teeth
•Jaw Surgery
•facial trauma
The goal of this billboard is to let our community know that they have an option here in Ada, our town. Many still drive to the city a couple hours away not knowing they now have an option here at home. Having a hard time finding examples of what I have in mind, so hoping this will get us going. I want it as “non-busy” as possible, so no unnecessary lines or anything that competes with the information we are trying to get across.

Target Market(s)

Everyone in town, just trying to spread the word that we are here

Industry/Entity Type

Medical/surgical (oral surgery)

Font styles to use
Sans Serif

Colors
0094D4
00A9DD
6FCCEA
C7EBF8
E9F6FB

Requirements
Must have
• *New note** Due to location of billboard, I prefer the photo of doctor to be on the left side. Must look neat and professional. Must highlight what we do.
Nice to have
• Our colors are a blue-green with silver, against black or white, but I’m flexible on this, I don’t necessarily need the colors highlighted. I’m also flexible on font style, just needs to be easy to read.
Should not have
• Distracting graphics, should not look like a dental office. That’s an issue we have is people thinking we are another dental office, we do not do any general dentistry, it’s surgery only.

```html
<!DOCTYPE html>
<html lang="en">
<head>
<meta charset="utf-8">
<title>Oral Surgery Billboard</title>
<link href="https://fonts.googleapis.com/css2?family=Jost:wght@500;600;700&family=Poppins:wght@600;700&display=swap" rel="stylesheet">
<style>
  :root {
    --page-bg: #a8a8a8;
    --white: #ffffff;
    --teal-green: #3b7d76;
    --brand-blue: #0b95b8;
    --charcoal: #242424;
    --ink: #111111;
    --silver: #c9cdd1;
    --logo-grey: #4a4f55;
  }
  * { margin: 0; padding: 0; box-sizing: border-box; }
  html, body {
    width: 915px; height: 1200px; overflow: hidden;
    background: var(--page-bg);
  }
  .billboard {
    position: absolute; left: 27px; top: 457px;
    width: 860px; height: 286px;
    background: var(--white);
    box-shadow: 4px 6px 12px rgba(0,0,0,.35);
    overflow: hidden;
    font-family: "Jost", sans-serif;
  }
  .tagline-band {
    position: absolute; left: 0; top: 137px; width: 100%; height: 46px;
    background: var(--teal-green);
  }
  .info-panel {
    position: absolute; left: 0; top: 185px; width: 100%; height: 101px;
    background: var(--charcoal);
  }
  .doctor-photo {
    position: absolute; left: 0; top: 0; width: 250px; height: 286px;
    background: linear-gradient(180deg, #f4efec 0%, #e9cdbd 35%, #d9b29c 55%, #1d2438 78%, #141a2a 100%);
  }
  .name-tag {
    position: absolute; left: 0; top: 245px; width: 220px; height: 41px;
    background: var(--brand-blue);
    clip-path: polygon(0 0, 190px 0, 220px 100%, 0 100%);
    color: var(--white);
    font-family: "Poppins", sans-serif; font-weight: 700; font-size: 16px;
    line-height: 41px; padding-left: 24px;
  }
  .headline {
    position: absolute; left: 259px; top: 22px;
    line-height: 1; white-space: nowrap;
  }
  .headline-main {
    display: block; color: var(--brand-blue);
    font-weight: 600; font-size: 58px; letter-spacing: 0.5px;
  }
  .headline-sub {
    display: block; color: var(--ink);
    font-weight: 600; font-size: 39.5px; margin-top: 2px;
  }
  .practice-mark {
    position: absolute; left: 712px; top: 22px; width: 130px;
    display: flex; flex-direction: column; align-items: center; gap: 12px;
  }
  .practice-mark .mark-dot {
    width: 54px; height: 54px; border-radius: 50%;
    background: var(--silver);
  }
  .practice-mark .mark-name {
    color: var(--logo-grey); font-weight: 500; font-size: 10.5px;
    line-height: 1.25; text-align: center; text-transform: uppercase;
  }
  .locale-line {
    position: absolute; left: 259px; top: 137px; width: 580px; height: 46px;
    color: var(--white); font-weight: 700; font-size: 33px;
    letter-spacing: 6.5px; line-height: 46px; white-space: nowrap;
  }
  .service-list {
    position: absolute; left: 263px; top: 195px; width: 570px;
    display: flex; gap: 4px; list-style: none;
  }
  .service-list li {
    flex: 1; height: 26px; line-height: 26px; text-align: center;
    color: var(--white); font-family: "Poppins", sans-serif;
    font-weight: 600; font-size: 12.5px; letter-spacing: .3px;
    background: var(--teal-green);
  }
  .service-list li:nth-child(even) { background: var(--brand-blue); }
  .contact-row {
    position: absolute; left: 266px; top: 232px; width: 570px; height: 34px;
    display: flex; align-items: center; color: var(--white);
  }
  .book-call {
    font-weight: 500; font-size: 23px; white-space: nowrap;
    display: flex; align-items: center; gap: 7px;
  }
  .book-call .phone-icon { width: 24px; height: 24px; }
  .book-call .phone-number { font-weight: 600; }
  .divider {
    width: 2px; height: 26px; background: var(--white); margin: 0 12px;
  }
  .address {
    display: flex; align-items: flex-start; gap: 6px;
    font-family: "Poppins", sans-serif; font-weight: 700;
    font-size: 11.5px; line-height: 1.2; white-space: nowrap;
  }
  .address .pin-icon { width: 11px; height: 14px; margin-top: 1px; }
</style>
</head>
<body>
  <section class="billboard">
    <div class="tagline-band"></div>
    <div class="info-panel"></div>

    <div class="doctor-photo" role="img" aria-label="Portrait photo of Dr. Tobin Marek smiling, wearing a dark suit and red tie"></div>
    <div class="name-tag">Tobin Marek, D.D.S.</div>

    <h1 class="headline">
      <span class="headline-main">ORAL SURGERY</span>
      <span class="headline-sub">&amp; COSMETIC SERVICES</span>
    </h1>

    <div class="practice-mark">
      <span class="mark-dot"></span>
      <span class="mark-name">Red River Oral<br>&amp; Facial Surgery</span>
    </div>

    <p class="locale-line">THE NEW LOCALE IN ADA</p>

    <ul class="service-list">
      <li>IMPLANTS</li>
      <li>WISDOM TEETH</li>
      <li>JAW SURGERY</li>
      <li>FACIAL TRAUMA</li>
    </ul>

    <div class="contact-row">
      <div class="book-call">
        <span>BOOK TODAY</span>
        <svg class="phone-icon" viewBox="0 0 24 24" aria-hidden="true">
          <circle cx="12" cy="12" r="12" fill="#3b7d76"/>
          <path d="M8.2 6.3c.4-.3.9-.2 1.1.2l1.1 2.1c.2.4.1.8-.2 1.1l-.8.7c.6 1.3 1.6 2.4 2.9 3.1l.8-.8c.3-.3.8-.4 1.1-.1l2 1.2c.4.2.5.8.2 1.1l-.9 1.1c-.5.6-1.3.8-2 .5-3-1.2-5.3-3.6-6.4-6.6-.3-.7 0-1.5.5-2z" fill="#242424"/>
        </svg>
        <span class="phone-number">(580) 555-0147</span>
      </div>
      <span class="divider"></span>
      <div class="address">
        <svg class="pin-icon" viewBox="0 0 12 16" aria-hidden="true">
          <path d="M6 0a5 5 0 0 0-5 5c0 3.6 5 9 5 9s5-5.4 5-9a5 5 0 0 0-5-5zm0 7a2 2 0 1 1 0-4 2 2 0 0 1 0 4z" fill="#0b95b8"/>
          <rect x="1" y="15" width="10" height="1" fill="#0b95b8"/>
        </svg>
        <span>412 W Cedar Ridge Ave. Ada,<br>OK 74821, USA</span>
      </div>
    </div>
  </section>
</body>
</html>
```